Need new sign at entrance for new fruit and vegetable wholesaler in market. Main vegetables sold are
Broccoli , Cauliflower , cabbage , capsicum , tomatoes , lettuce .
Business name is Tenby Crop
I have included examples of other designs and a sketch of suggested layout.
Business

```html
<!DOCTYPE html>
<html lang="en">
<head>
<meta charset="utf-8">
<title>Tenby Crop – Entrance Sign</title>
<link rel="stylesheet" href="https://fonts.googleapis.com/css2?family=Chewy&family=Arimo:wght@700&display=swap">
<style>
  :root {
    --lime: #a9cd2c;
    --lime-deep: #9cc226;
    --leaf-dark: #5a7d3a;
    --ink-green: #1f3a0e;
    --title-fill: #ececec;
    --white: #ffffff;
    --tile-shadow: #4a4a4a;
    --panel-shadow: #8a8a8a;
    --black: #111111;
  }
  * { box-sizing: border-box; margin: 0; padding: 0; }
  html, body { width: 1200px; height: 335px; overflow: hidden; background: var(--white); }

  .sign {
    position: relative;
    width: 1200px;
    height: 335px;
    overflow: hidden;
    background: radial-gradient(ellipse at 40% 40%, var(--lime) 0%, var(--lime-deep) 100%);
  }

  .business-name {
    position: absolute;
    left: 0;
    top: 0;
    width: 900px;
    height: 190px;
  }
  .business-name text {
    font-family: "Chewy", "Comic Sans MS", cursive;
    font-size: 150px;
    stroke-linejoin: round;
  }
  .name-halo { fill: var(--white); stroke: var(--white); stroke-width: 24px; }
  .name-edge { fill: var(--leaf-dark); stroke: var(--leaf-dark); stroke-width: 11px; }
  .name-face { fill: var(--title-fill); }

  .location {
    position: absolute;
    left: 970px;
    top: 52px;
    font-family: "Arimo", Arial, sans-serif;
    font-weight: 700;
    font-size: 29px;
    line-height: 41px;
    letter-spacing: 2px;
    color: var(--white);
    -webkit-text-stroke: 1.5px var(--black);
    text-shadow: 1px 1px 0 var(--black), -1px -1px 0 var(--black), 1px -1px 0 var(--black), -1px 1px 0 var(--black);
  }
  .location .shed { padding-left: 12px; word-spacing: 14px; }

  .produce {
    position: absolute;
    left: 28px;
    top: 206px;
    display: flex;
    gap: 8px;
  }
  .produce-tile {
    width: 124px;
    height: 112px;
    background: var(--white);
    border-radius: 7px;
    box-shadow: 4px 4px 0 var(--tile-shadow);
    padding: 8px;
  }
  .produce-photo {
    width: 100%;
    height: 100%;
    border-radius: 40%;
  }
  .photo-tomato { background: radial-gradient(circle at 45% 55%, #e23a22 0%, #c8261a 55%, #ffffff 72%); }
  .photo-broccoli { background: radial-gradient(circle at 50% 50%, #477f22 0%, #2f5e17 55%, #ffffff 74%); }
  .photo-cabbage { background: radial-gradient(circle at 50% 50%, #c6e29c 0%, #97c662 55%, #ffffff 74%); }
  .photo-cauliflower { background: radial-gradient(circle at 50% 50%, #f4eedc 0%, #e0d6b5 55%, #ffffff 74%); }
  .photo-lettuce { background: radial-gradient(circle at 50% 50%, #74c23a 0%, #4f9a22 55%, #ffffff 74%); }
  .photo-capsicum { background: radial-gradient(circle at 35% 60%, #c92a1c 0%, #c92a1c 25%, transparent 45%), radial-gradient(circle at 68% 52%, #2f7a1c 0%, #2f7a1c 28%, #ffffff 50%); }

  .contact-panel {
    position: absolute;
    left: 0;
    top: 0;
    width: 1200px;
    height: 335px;
    pointer-events: none;
  }

  .contact {
    position: absolute;
    left: 848px;
    top: 222px;
    width: 330px;
    text-align: center;
    font-family: "Arimo", Arial, sans-serif;
    font-weight: 700;
    color: var(--lime);
    -webkit-text-stroke: 1.6px var(--ink-green);
    letter-spacing: 3px;
  }
  .contact-label { font-size: 37px; line-height: 44px; }
  .contact-number { font-size: 42px; line-height: 56px; word-spacing: 6px; }
</style>
</head>
<body>
<main class="sign">
  <svg class="business-name" viewBox="0 0 900 190" role="img" aria-label="Tenby Crop">
    <text class="name-halo" x="40" y="145" textLength="840" lengthAdjust="spacingAndGlyphs" aria-hidden="true">Tenby Crop</text>
    <text class="name-edge" x="40" y="145" textLength="840" lengthAdjust="spacingAndGlyphs" aria-hidden="true">Tenby Crop</text>
    <text class="name-face" x="40" y="145" textLength="840" lengthAdjust="spacingAndGlyphs">Tenby Crop</text>
  </svg>

  <div class="location">
    <div>STAND 214</div>
    <div class="shed">C SHED</div>
  </div>

  <section class="produce" aria-label="Vegetables sold">
    <div class="produce-tile"><div class="produce-photo photo-tomato" role="img" aria-label="Photo of fresh tomatoes"></div></div>
    <div class="produce-tile"><div class="produce-photo photo-broccoli" role="img" aria-label="Photo of broccoli"></div></div>
    <div class="produce-tile"><div class="produce-photo photo-cabbage" role="img" aria-label="Photo of cabbage"></div></div>
    <div class="produce-tile"><div class="produce-photo photo-cauliflower" role="img" aria-label="Photo of cauliflower"></div></div>
    <div class="produce-tile"><div class="produce-photo photo-lettuce" role="img" aria-label="Photo of lettuce"></div></div>
    <div class="produce-tile"><div class="produce-photo photo-capsicum" role="img" aria-label="Photo of red, yellow and green capsicums"></div></div>
  </section>

  <svg class="contact-panel" viewBox="0 0 1200 335" aria-hidden="true">
    <path d="M 812 335 Q 808 208 960 194 Q 1080 184 1200 180 V 335 Z" fill="var(--panel-shadow)" transform="translate(-4,-3)"/>
    <path d="M 818 335 Q 814 212 964 198 Q 1082 188 1200 185 V 335 Z" fill="var(--white)"/>
  </svg>

  <div class="contact">
    <div class="contact-label">Phone/Fax</div>
    <div class="contact-number">02 5550 1947</div>
  </div>
</main>
</body>
</html>
```